Business Card + Letterhead Design for BELMARSH IMPORTS INC.

We already have a logo; now we need a business card + letterhead. We import and distribute flags and souvenirs with an emphasis on soccer related memorabilia. We target various ethnic markets and sporting goods stores. "Wandering Keepsakes"

```html
<!DOCTYPE html>
<html lang="en">
<head>
<meta charset="utf-8">
<title>Belmarsh Imports Inc. — Stationery</title>
<link href="https://fonts.googleapis.com/css2?family=Montserrat:wght@500;600;700&display=swap" rel="stylesheet">
<style>
  :root {
    --backdrop: #e6e3df;
    --paper: #ffffff;
    --ink: #1b1b1b;
    --ink-soft: #3a3a3a;
    --brand-red: #8c1c1c;
    --watermark: #f1f1f1;
    --muted: #6b6b6b;
  }
  * { box-sizing: border-box; margin: 0; padding: 0; }
  html, body {
    width: 1200px; height: 675px; overflow: hidden;
    background: var(--backdrop);
    font-family: "Montserrat", Arial, sans-serif;
    color: var(--ink);
  }
  .stationery { position: relative; width: 1200px; height: 675px; }

  /* shared brand lockup */
  .brand { display: flex; align-items: center; gap: 8px; }
  .brand-dot { width: 14px; height: 14px; border-radius: 50%; background: var(--ink); flex: none; }
  .brand-name {
    font-weight: 700; font-size: 13px; letter-spacing: 1.5px;
    color: var(--ink); text-transform: uppercase; white-space: nowrap;
  }
  .rule-pair { flex: 1; display: flex; flex-direction: column; gap: 2px; }
  .rule-pair .rule-dark { height: 3px; background: var(--ink); }
  .rule-pair .rule-red { height: 1px; background: var(--brand-red); }

  /* letterhead */
  .letterhead {
    position: absolute; left: 90px; top: 38px; width: 425px; height: 600px;
    background: var(--paper); box-shadow: 0 2px 10px rgba(0,0,0,.18); overflow: hidden;
  }
  .letterhead-header { position: absolute; left: 18px; right: 0; top: 36px; }
  .letterhead-watermark {
    position: absolute; left: 110px; top: 190px; width: 140px; height: 140px;
    border-radius: 50%; background: var(--watermark);
  }
  .letterhead-footer {
    position: absolute; left: 0; right: 0; bottom: 0; height: 48px;
    background: var(--ink); color: var(--paper);
    display: flex; flex-direction: column; align-items: flex-end; justify-content: center;
    padding-right: 26px; gap: 2px;
    font-size: 6.5px; font-weight: 600; letter-spacing: .6px; text-transform: uppercase;
  }

  /* business card front */
  .card-front {
    position: absolute; left: 580px; top: 60px; width: 290px; height: 166px;
    background: var(--paper); box-shadow: 0 2px 8px rgba(0,0,0,.18);
  }
  .card-name-tag {
    position: absolute; left: 10px; top: 8px; width: 86px; height: 30px;
    background: var(--ink); color: var(--paper); border-radius: 2px;
    display: flex; flex-direction: column; align-items: center; justify-content: center; gap: 2px;
  }
  .card-name { font-size: 7px; font-weight: 700; letter-spacing: .4px; text-transform: uppercase; }
  .card-title { font-size: 5.5px; font-weight: 500; }
  .card-brand {
    position: absolute; right: 16px; top: 10px;
    display: flex; flex-direction: column; align-items: center; gap: 4px;
  }
  .card-brand .brand-dot { width: 16px; height: 16px; }
  .card-brand .brand-name { font-size: 7px; letter-spacing: .6px; }
  .card-contacts {
    position: absolute; left: 108px; top: 70px; list-style: none;
    display: flex; flex-direction: column; gap: 5px;
  }
  .card-contacts li { display: flex; align-items: center; gap: 7px; font-size: 7px; font-weight: 500; color: var(--ink-soft); }
  .card-contacts svg { width: 7px; height: 7px; flex: none; }
  .card-tagline {
    position: absolute; left: 112px; bottom: 0; width: 124px; height: 13px;
    background: var(--ink); color: var(--paper); border-radius: 2px 2px 0 0;
    font-size: 5.5px; font-weight: 600; letter-spacing: .6px;
    display: flex; align-items: center; justify-content: center;
  }

  /* business card back */
  .card-back {
    position: absolute; left: 890px; top: 60px; width: 290px; height: 166px;
    background: var(--ink); box-shadow: 0 2px 8px rgba(0,0,0,.25);
    display: flex; align-items: center; justify-content: center;
  }
  .card-back .brand-dot { width: 30px; height: 30px; background: #4a4a4a; }
  .card-back .brand-name { font-size: 17px; color: #4a4a4a; letter-spacing: 2px; }
  .card-back .brand { gap: 12px; }

  /* envelope */
  .envelope {
    position: absolute; left: 580px; top: 290px; width: 600px; height: 260px;
    background: var(--paper); box-shadow: 0 2px 10px rgba(0,0,0,.18); overflow: hidden;
  }
  .envelope-flap { position: absolute; left: 0; top: 0; width: 600px; height: 36px; }
  .envelope-watermark {
    position: absolute; right: 60px; top: 40px; width: 180px; height: 180px;
    border-radius: 50%; background: var(--watermark);
  }
  .envelope-brand { position: absolute; left: 14px; right: 0; top: 142px; }
  .envelope-brand .brand-dot { width: 22px; height: 22px; }
  .envelope-brand .brand-name { font-size: 15px; letter-spacing: 2px; }
</style>
</head>
<body>
<main class="stationery">

  <section class="letterhead" aria-label="Letterhead">
    <div class="letterhead-watermark"></div>
    <header class="letterhead-header brand">
      <span class="brand-dot"></span>
      <span class="brand-name">Belmarsh Imports</span>
      <span class="rule-pair"><span class="rule-dark"></span><span class="rule-red"></span></span>
    </header>
    <footer class="letterhead-footer">
      <p>Address: 880-14 Harrow Lane, Toronto, ON, Canada M5V 2K9</p>
      <p>Phone: (555) 210-3391 &nbsp;Fax: (555) 480-7720 &nbsp;Email: sales@belmarshimports.ca</p>
      <p>Web: belmarshimports.ca</p>
    </footer>
  </section>

  <section class="card-front" aria-label="Business card front">
    <div class="card-name-tag">
      <span class="card-name">Daniel Ostrava</span>
      <span class="card-title">President</span>
    </div>
    <div class="card-brand">
      <span class="brand-dot"></span>
      <span class="brand-name">Belmarsh Imports Inc.</span>
    </div>
    <ul class="card-contacts">
      <li>
        <svg viewBox="0 0 10 10" aria-hidden="true"><path d="M2 1 L4 1 L4.5 3 L3.3 3.8 Q4.5 6 6.2 6.7 L7 5.5 L9 6 L9 8 Q5 9 2 4.5 Q1.4 3 2 1 Z" fill="#3a3a3a"/></svg>
        (555) 210-3391
      </li>
      <li>
        <svg viewBox="0 0 10 10" aria-hidden="true"><rect x="2" y="1" width="6" height="3" fill="none" stroke="#3a3a3a"/><rect x="1" y="4" width="8" height="4" fill="#3a3a3a"/></svg>
        (555) 480-7720
      </li>
      <li>
        <svg viewBox="0 0 10 10" aria-hidden="true"><rect x="1" y="2" width="8" height="6" fill="none" stroke="#3a3a3a"/><path d="M1 2 L5 5.5 L9 2" fill="none" stroke="#3a3a3a"/></svg>
        sales@belmarshimports.ca
      </li>
    </ul>
    <div class="card-tagline">Wandering Keepsakes</div>
  </section>

  <section class="card-back" aria-label="Business card back">
    <div class="brand">
      <span class="brand-dot"></span>
      <span class="brand-name">Belmarsh Imports</span>
    </div>
  </section>

  <section class="envelope" aria-label="Envelope">
    <div class="envelope-watermark"></div>
    <svg class="envelope-flap" viewBox="0 0 600 36" preserveAspectRatio="none" aria-hidden="true">
      <polygon points="0,36 18,0 582,0 600,36" fill="#1b1b1b"/>
    </svg>
    <div class="envelope-brand brand">
      <span class="brand-dot"></span>
      <span class="brand-name">Belmarsh Imports</span>
      <span class="rule-pair"><span class="rule-dark"></span><span class="rule-red"></span></span>
    </div>
  </section>

</main>
</body>
</html>
```